Website Redesign for Accommodation Directory

We need a redesign for stayfinderhubzone.example
The new design needs to include a banner with overlaid text and a 'get started now' button. The overlaid text could be 'Find Hotels in Auckland, New Zealand' for example.
The new design needs to include:
- primary navigation in header
- an accommodation search (left or right column)
- a secondary navigation menu (under the search).
We will need the following font styles (including links for each) defined also please:
h1, h2, h3, h4, h5, h6, p, ul, ol, address, pre
Accommodation

```html
<!DOCTYPE html>
<html lang="en">
<head>
<meta charset="utf-8">
<title>StayFinder Hub Zone – Accommodation Directory</title>
<link rel="stylesheet" href="https://fonts.googleapis.com/css2?family=PT+Sans:wght@400;700&family=Open+Sans:wght@400&family=Questrial&display=swap">
<style>
  :root{
    --brand-red:#a8280e;
    --banner-red:#a0290e;
    --ink-dark:#3b332d;
    --nav-1:#3b332d;
    --nav-2:#4a3f38;
    --nav-3:#544a43;
    --nav-4:#615750;
    --nav-5:#6e645d;
    --search-bar:#343434;
    --field:#dcdcdc;
    --panel:#3a3029;
    --text:#1f1f1f;
    --grey:#5a5a5c;
    --page-top:#f2e4e2;
    --page-bottom:#ffffff;
  }
  *{box-sizing:border-box;margin:0;padding:0}
  html,body{width:1070px;height:1200px;overflow:hidden}
  body{
    position:relative;
    font-family:"PT Sans",Arial,sans-serif;
    color:var(--text);
    background:linear-gradient(to bottom,var(--page-top) 0,#f8f0ef 420px,#fcfafa 660px,var(--page-bottom) 760px);
  }
  .abs{position:absolute}

  /* header */
  .brand-name{left:110px;top:28px;font-family:"PT Sans",Arial,sans-serif;font-weight:400;font-size:54px;line-height:60px;color:var(--grey)}
  .brand-url{left:112px;top:92px;font-family:"PT Sans",Arial,sans-serif;font-weight:400;font-size:15px;line-height:18px;color:var(--grey)}

  .home-link{left:132px;top:149px;width:56px;height:46px}
  .primary-nav{left:208px;top:146px;width:665px;height:58px;display:flex}
  .primary-nav a{flex:1;display:flex;align-items:center;justify-content:center;color:#fff;text-decoration:none;font-size:15px;text-transform:uppercase}
  .primary-nav a:nth-child(1){background:var(--nav-1)}
  .primary-nav a:nth-child(2){background:var(--nav-2)}
  .primary-nav a:nth-child(3){background:var(--nav-3)}
  .primary-nav a:nth-child(4){background:var(--nav-4)}
  .primary-nav a:nth-child(5){background:var(--nav-5)}
  .nav-rule{left:208px;top:205px;width:665px;height:6px;background:var(--brand-red)}

  /* banner */
  .side-frame{background:#3a3029}
  .side-frame.left{left:29px;top:297px;width:179px;height:223px}
  .side-frame.right{left:874px;top:297px;width:161px;height:223px}
  .side-photo.left{left:41px;top:286px;width:167px;height:222px;background:linear-gradient(135deg,#b9b6ae,#7e7a6f 55%,#d8d3c7)}
  .side-photo.right{left:874px;top:286px;width:149px;height:222px;background:linear-gradient(160deg,#3b3c3f,#6b6a6a 45%,#d9d6d2 80%)}
  .hero-photo{left:208px;top:214px;width:665px;height:372px;background:linear-gradient(160deg,#8c1f1c 0,#c8474a 20%,#6e6566 45%,#8a1d1f 70%,#d6d2d0 100%)}
  .hero-bar{left:208px;top:586px;width:665px;height:39px;background:var(--banner-red);display:flex;align-items:center;padding:0 10px 0 12px}
  .slide-dots{display:flex;gap:10px;list-style:none}
  .slide-dots li{width:25px;height:25px;border-radius:50%;background:#fff;color:var(--banner-red);font-size:13px;display:flex;align-items:center;justify-content:center}
  .hero-caption{margin-left:auto;color:#fff;font-family:Arial,sans-serif;font-size:15px}
  .slide-btn{height:21px;background:var(--brand-red);color:#fff;font-size:15px;display:flex;align-items:center;justify-content:center;gap:5px;text-decoration:none}
  .slide-btn.prev{left:126px;top:557px;width:80px}
  .slide-btn.next{left:874px;top:560px;width:77px}

  /* search */
  .search-bar{left:15px;top:677px;width:1055px;height:61px;background:var(--search-bar);border-radius:8px 0 0 8px}
  .search-label{left:36px;top:695px;color:#fff;font-size:17px}
  .select{top:690px;width:233px;height:30px;background:var(--field);font-size:11px;color:#555;display:flex;align-items:center;padding-left:12px}
  .select.country{left:97px}
  .select.category{left:340px}
  .select svg{position:absolute;right:10px;top:11px}
  .search-btn{left:580px;top:690px;width:86px;height:30px;background:var(--brand-red);color:#fff;font-size:16px;display:flex;align-items:center;justify-content:center}
  .get-started{left:750px;top:677px;width:264px;height:61px;background:linear-gradient(to bottom,#f4f4f4,#d8d8d8);display:flex;align-items:center;justify-content:center;gap:12px;font-family:"Questrial",Arial,sans-serif;font-size:23px;color:#333;text-decoration:none}

  /* listings */
  .thumb{width:124px;height:113px;box-shadow:2px 4px 8px rgba(0,0,0,.35);border:1px solid #999}
  .thumb.one{left:24px;top:773px;background:linear-gradient(135deg,#6b5446,#d2c8bc 50%,#48413b)}
  .thumb.two{left:23px;top:938px;background:linear-gradient(135deg,#d9d3c6,#9a8a76 55%,#5c4030)}
  .listing-text{left:170px;width:510px;font-family:"Open Sans",Tahoma,sans-serif;font-size:12.6px;line-height:16.6px;color:#111}
  .listing-text.one{top:776px}
  .listing-text.two{top:941px}
  .read-more{width:78px;height:23px;background:var(--ink-dark);color:#fff;font-size:13px;display:flex;align-items:center;justify-content:center;text-decoration:none}
  .read-more.one{left:596px;top:869px}
  .read-more.two{left:596px;top:1035px}
  .rule-h{border-top:1px dashed #333}
  .rule-h.mid{left:33px;top:918px;width:637px}
  .rule-h.foot{left:24px;top:1088px;width:1022px}
  .rule-v{left:697px;top:771px;height:291px;border-left:1px dashed #333}

  /* secondary navigation */
  .tabs{left:772px;top:775px;display:flex;gap:5px}
  .tabs span{height:24px;border-radius:6px 6px 0 0;color:#fff;font-size:14px;display:flex;align-items:center;justify-content:center;background:var(--brand-red)}
  .tabs .active{background:var(--panel);width:76px}
  .tabs .news{width:75px}
  .tabs .navigator{width:105px}
  .panel{left:711px;top:798px;width:343px;height:262px;background:var(--panel);border-radius:10px;padding:24px 22px 0 17px;color:#fff;font-family:"Open Sans",Tahoma,sans-serif;font-size:12.6px;line-height:16.6px}
  .panel-more{left:931px;top:1019px;display:flex;align-items:center;gap:8px;color:#fff;font-size:13px}
  .panel-more a{color:#fff}
  .panel-more a span{color:#e2643f}

  /* footer */
  .footer-nav{left:0;top:1122px;width:1070px;text-align:center;font-family:Arial,sans-serif;font-size:14px}
  .footer-nav a{color:#111;text-decoration:none;margin:0 9px}
  .copyright{left:0;top:1153px;width:1070px;text-align:center;font-family:Arial,sans-serif;font-size:14px;color:#111}

  /* type styles */
  h1{font-size:28px}h2{font-size:24px}h3{font-size:20px}h4{font-size:17px}h5{font-size:15px}h6{font-size:13px}
  p,ul,ol,address,pre{font-size:13px}
  a{color:var(--brand-red)}
</style>
</head>
<body>
  <header>
    <div class="abs brand-name">StayFinder Hub Zone</div>
    <div class="abs brand-url">stayfinderhubzone.example</div>

    <a class="abs home-link" href="#" aria-label="Home">
      <svg width="56" height="46" viewBox="0 0 56 46"><path d="M4 22 L28 3 L52 22" fill="none" stroke="#c8231d" stroke-width="5" stroke-linejoin="round"/><rect x="38" y="5" width="6" height="10" fill="#c8231d"/><path d="M11 22 L28 9 L45 22 V44 H33 V31 H23 V44 H11 Z" fill="#c8231d"/></svg>
    </a>
    <nav class="abs primary-nav">
      <a href="#">About Us</a><a href="#">Add Property</a><a href="#">Login</a><a href="#">Search</a><a href="#">Contact</a>
    </nav>
    <div class="abs nav-rule"></div>
  </header>

  <section class="banner">
    <div class="abs side-frame left"></div>
    <div class="abs side-photo left" role="img" aria-label="Living room with white sofa"></div>
    <div class="abs side-frame right"></div>
    <div class="abs side-photo right" role="img" aria-label="Modern bedroom interior"></div>
    <div class="abs hero-photo" role="img" aria-label="Modern lounge with red sofas and red ceiling"></div>
    <div class="abs hero-bar">
      <ol class="slide-dots"><li>1</li><li>2</li><li>3</li><li>4</li><li>5</li></ol>
      <span class="hero-caption">Find Hotels in Auckland, New Zealand</span>
    </div>
    <a class="abs slide-btn prev" href="#"><svg width="16" height="11" viewBox="0 0 16 11"><path d="M7 1 L2 5.5 L7 10 M14 1 L9 5.5 L14 10" fill="none" stroke="#fff" stroke-width="2.4"/></svg>Prev</a>
    <a class="abs slide-btn next" href="#">Next<svg width="16" height="11" viewBox="0 0 16 11"><path d="M2 1 L7 5.5 L2 10 M9 1 L14 5.5 L9 10" fill="none" stroke="#fff" stroke-width="2.4"/></svg></a>
  </section>

  <section class="search">
    <div class="abs search-bar"></div>
    <span class="abs search-label">Search</span>
    <div class="abs select country">All Countries<svg width="16" height="9"><path d="M0 0 H16 L8 9 Z" fill="#555"/></svg></div>
    <div class="abs select category">All Categories<svg width="16" height="9"><path d="M0 0 H16 L8 9 Z" fill="#555"/></svg></div>
    <div class="abs search-btn">Search</div>
    <a class="abs get-started" href="#">GET STARTED NOW<svg width="30" height="20" viewBox="0 0 30 20"><path d="M0 7 H17 V1 L29 10 L17 19 V13 H0 Z" fill="#b8331a"/></svg></a>
  </section>

  <main>
    <div class="abs thumb one" role="img" aria-label="Hotel bedroom with brown curtains"></div>
    <p class="abs listing-text one">Lorem Ipsum is simply dummy text of the printing and typesetting industry. Lorem Ipsum has been the industry's standard dummy text ever since the 1500s, when an unknown printer took a galley of type and scrambled it to make a type specimen book. Ipsum has been the industry's standard dummy text ever since the 1500s, when an unknown printer took a galley of type and scrambled it to make a type specimen book</p>
    <a class="abs read-more one" href="#">Read More</a>
    <div class="abs rule-h mid"></div>
    <div class="abs thumb two" role="img" aria-label="Bright apartment living room"></div>
    <p class="abs listing-text two">Lorem Ipsum is simply dummy text of the printing and typesetting industry. Lorem Ipsum has been the industry's standard dummy text ever since the 1500s, when an unknown printer took a galley of type and scrambled it to make a type specimen book. Ipsum has been the industry's standard dummy text ever since the 1500s, when an unknown printer took a galley of type and scrambled it to make a type specimen book</p>
    <a class="abs read-more two" href="#">Read More</a>
    <div class="abs rule-v"></div>

    <aside>
      <div class="abs tabs"><span class="active">Location</span><span class="news">News</span><span class="navigator">Navigator</span></div>
      <div class="abs panel">Lorem Ipsum is simply dummy text of the print­ing and typesetting industry. Lorem Ipsum has been the industry's standard dummy text ever since the 1500s, when an unknown printer took a galley of type and scrambled it to make a type specimen book. Ipsum has been the industry's standard dummy text ever since the 1500s, when an unknown printer took a galley of type and scrambled it to make a type specimen book took a galley of type when an unknown printer and scrambled it to make a type specimen book.</div>
      <div class="abs panel-more"><svg width="22" height="22" viewBox="0 0 22 22"><circle cx="11" cy="11" r="10" fill="#fff"/><path d="M8 6 L13 11 L8 16" fill="none" stroke="#3a3029" stroke-width="2.6"/></svg><a href="#">Read <span>More</span></a></div>
    </aside>
  </main>

  <footer>
    <div class="abs rule-h foot"></div>
    <nav class="abs footer-nav"><a href="#">Home</a>|<a href="#">About Us</a>|<a href="#">Add Property</a>|<a href="#">Login</a>|<a href="#">Search</a>|<a href="#">Contact Us</a></nav>
    <p class="abs copyright">Copyright © 2011 StayFinder Hub Zone</p>
  </footer>
</body>
</html>
```